new branding The Velvet Pour Society

The Velvet Pour Society is a Belgian brand of ready to serve mocktails. We're looking for a rebranding of the labels on our bottles (8 different flavours)
Our mocktails are low in sugar, 100% natural and completely alcohol-free. They are also 'ready to serve': gently shake the bottle, serve with ice cubes, finish and your mocktail is ready in no time!
Besides being the ideal aperitif, you can also serve them during brunch or dinner. Thanks to the different flavors, you can pair each mocktail with a dish.
Please visit our website to see the current look&feel: the velvetpoursociety.com - https://thevelvetpoursociety.glimmerfold.com/

Target Market(s)

people looking for a premium alcoholfree alternative - premium market

Industry/Entity Type

Mocktails (our mocktails have unique flavors, it's not the non-alcoholic version of a cocktail)

Colors

Designer to choose colors to be used in the design.

Requirements
Must have
• Our brand should be more visible, more recognizable, bolder, without losing the premium and refined character. Base colors should be white, black and silver. The brand should be put more foward. Keep number concept (every mocktail has its number) Put the ingredients/flavours/combinations a bit more forward. make the brand more confident and mature. The eight bottles should become a family. PREMIUM EXPRESSION
Nice to have
• We want to work with a white label. Ideas for the shape of the label Some ideas for the label: Play with shapes, cut outs, texture and number of labels. We like the frosted look and the combination of print & label . Working with 2 labels gives it more dynamic, not one big block Clean label. Working with a cut out shape, can be the logo or the numbers ? Working with 2 labels makes it easier to create an importance of messages. Working with an organic shape makes it unique and give a natural touch Working with a cut out can give a color pop on the white label The label can have parts coming out of the square shape
Should not have
• No crazy stuff, finishes etc should be feasible/realistic

```html
<!DOCTYPE html>
<html lang="en">
<head>
<meta charset="utf-8">
<title>The Velvet Pour Society — Premium Expression Label</title>
<link rel="stylesheet" href="https://fonts.googleapis.com/css2?family=Mulish:wght@600;700;900&display=swap">
<style>
  :root {
    --backdrop: #e9e9e9;
    --label-white: #ffffff;
    --ink: #111111;
    --rule-silver: #c6c6c6;
    --ornament-tint: #efefef;
    --ornament-fade: #f8f8f8;
  }
  * { margin: 0; padding: 0; box-sizing: border-box; }
  html, body {
    width: 1200px;
    height: 1200px;
    overflow: hidden;
    background: var(--backdrop);
  }
  .canvas {
    position: relative;
    width: 1200px;
    height: 1200px;
  }
  .label {
    position: absolute;
    left: 254px;
    top: 80px;
    width: 694px;
    height: 1039px;
    background: var(--label-white);
    font-family: "Mulish", sans-serif;
    color: var(--ink);
    overflow: hidden;
  }
  .floral-motif {
    position: absolute;
    left: 0;
    top: 240px;
    width: 272px;
    height: 555px;
    background: radial-gradient(ellipse at 40% 50%, var(--ornament-tint) 0%, var(--ornament-fade) 60%, var(--label-white) 100%);
  }
  .brand-name {
    position: absolute;
    left: 0;
    right: 0;
    top: 112px;
    text-align: center;
    font-weight: 900;
    font-size: 56px;
    line-height: 1.55;
    letter-spacing: 0.04em;
    text-transform: uppercase;
  }
  .range-title {
    position: absolute;
    left: 0;
    right: 0;
    top: 448px;
    text-align: center;
    font-weight: 700;
    font-size: 33px;
    line-height: 46px;
    letter-spacing: 0.2em;
    text-transform: uppercase;
  }
  .spec-grid {
    position: absolute;
    left: 0;
    top: 0;
    width: 694px;
    height: 1039px;
  }
  .spec-grid line {
    stroke: var(--rule-silver);
    stroke-width: 3;
  }
  .spec-text {
    position: absolute;
    font-weight: 700;
    font-size: 31px;
    line-height: 45px;
  }
  .spec-alcohol {
    left: 136px;
    top: 762px;
    width: 180px;
    text-align: center;
  }
  .spec-flavour {
    left: 383px;
    top: 729px;
  }
  .spec-volume {
    left: 380px;
    top: 844px;
  }
</style>
</head>
<body>
  <main class="canvas">
    <section class="label">
      <div class="floral-motif" role="img" aria-label="Faint pale-grey floral branch ornament along the left edge of the label"></div>

      <h1 class="brand-name">The Velvet Pour<br>Society</h1>

      <p class="range-title">Premium<br>Expression</p>

      <svg class="spec-grid" viewBox="0 0 694 1039" aria-hidden="true">
        <line x1="346" y1="698" x2="346" y2="921"/>
        <line x1="124" y1="920" x2="347" y2="920"/>
        <line x1="345" y1="809" x2="568" y2="809"/>
      </svg>

      <p class="spec-text spec-alcohol">Non<br>Alcoholic</p>
      <p class="spec-text spec-flavour">Flavour</p>
      <p class="spec-text spec-volume">16 Fl oz</p>
    </section>
  </main>
</body>
</html>
```